Wedding Decor and Entertianment business card

Company - We run a weddings and events company called Amber Fern, we provide most entertainment and decor services to our customers.

Initial idea is ....
A simple business card with logo on the front, this will be spot varnish. On a matt black background.
The reverse will be simple contact information.

But happy to try things outside of the box and would welcome some crazy ideas.

Target Market(s)

wedding couples - 21 - 40
High end wedding venues.

Industry/Entity Type

Wedding

Contact Information for Business Card

01742 918 263
amberfern.co.uk
rupert@amberfern.co.uk
or
eleanor@amberfern.co.uk

Requirements
Nice to have
• black matt background with spot varnish logo on the front.

```html
<!DOCTYPE html>
<html lang="en">
<head>
<meta charset="utf-8">
<title>Amber Fern – Business Card</title>
<link rel="stylesheet" href="https://fonts.googleapis.com/css2?family=Jost:wght@400&family=Source+Sans+3:wght@400;600&display=swap">
<style>
  :root {
    --stage: #000000;
    --card-light: #d9d9d9;
    --card-plum: #835a7b;
    --plum: #7e4f74;
    --ink: #2e2e2e;
    --ink-soft: #444444;
    --white: #ffffff;
  }
  * { margin: 0; padding: 0; box-sizing: border-box; }
  html, body { width: 1200px; height: 900px; overflow: hidden; background: var(--stage); }
  .stage { position: relative; width: 1200px; height: 900px; }

  .card { position: absolute; top: 200px; width: 310px; height: 502px; }
  .card--contact {
    left: 265px; background: var(--card-light);
    border-radius: 50px 0 50px 0;
  }
  .card--brand {
    left: 621px; width: 309px; background: var(--card-plum);
    border-radius: 0 50px 0 50px;
  }

  .brand-mark {
    position: absolute; left: 50%; top: 44px; transform: translateX(-50%);
    width: 58px; height: 58px; border-radius: 50%;
    border: 4px solid var(--ink);
  }
  .wordmark {
    position: absolute; left: 0; right: 0; text-align: center;
    font-family: "Jost", sans-serif; font-weight: 400;
    font-size: 24px; letter-spacing: 5px; white-space: nowrap;
  }
  .card--contact .wordmark { top: 152px; color: var(--plum); padding-left: 6px; }
  .card--brand .wordmark { top: 401px; color: var(--white); padding-left: 5px; }

  .contacts {
    position: absolute; left: 36px; top: 259px;
    font-family: "Source Sans 3", sans-serif; color: var(--ink-soft);
    font-size: 14.5px; line-height: 18px;
  }
  .person { margin-bottom: 23px; }
  .person__name { color: var(--plum); font-weight: 600; font-size: 18px; line-height: 24px; }
  .line { display: flex; align-items: center; gap: 6px; }
  .line svg { width: 11px; height: 11px; flex: none; fill: var(--plum); }
  .general { margin-top: 1px; }
  .address { margin-top: 18px; }
</style>
</head>
<body>
<main class="stage">
  <section class="card card--contact">
    <span class="brand-mark" aria-hidden="true"></span>
    <div class="wordmark">AMBER FERN</div>

    <div class="contacts">
      <div class="person">
        <div class="person__name">Eleanor Marsh</div>
        <div class="line">
          <svg viewBox="0 0 12 12" aria-hidden="true"><path d="M1 2.5h10v7H1z"/><path d="M1 2.5l5 4 5-4" fill="none" stroke="#d9d9d9" stroke-width="1"/></svg>
          <span>eleanor@amberfern.co.uk</span>
        </div>
      </div>
      <div class="person">
        <div class="person__name">Rupert Marsh</div>
        <div class="line">
          <svg viewBox="0 0 12 12" aria-hidden="true"><path d="M1 2.5h10v7H1z"/><path d="M1 2.5l5 4 5-4" fill="none" stroke="#d9d9d9" stroke-width="1"/></svg>
          <span>rupert@amberfern.co.uk</span>
        </div>
      </div>

      <div class="general">
        <div class="line">
          <svg viewBox="0 0 12 12" aria-hidden="true"><path d="M2.5 1l2 2.5-1.2 1.4c.7 1.5 1.8 2.6 3.3 3.3l1.4-1.2 2.5 2-1.3 2C5 10.5 1.5 7 1 2.3z"/></svg>
          <span>01742 918 263</span>
        </div>
        <div class="line">
          <svg viewBox="0 0 12 12" aria-hidden="true"><circle cx="6" cy="6" r="5"/><path d="M1 6h10M6 1c-2.5 3-2.5 7 0 10M6 1c2.5 3 2.5 7 0 10" fill="none" stroke="#d9d9d9" stroke-width=".8"/></svg>
          <span>amberfern.co.uk</span>
        </div>
      </div>

      <address class="address" style="font-style:normal">
        unit 12b larkfield barns,<br>worcs, WR74QD
      </address>
    </div>
  </section>

  <section class="card card--brand">
    <div class="wordmark">AMBER FERN</div>
  </section>
</main>
</body>
</html>
```